Flyer-Design für Werbeflyer Teamentwicklung/Coaching als pdf
Zielgruppe
ich berate Personen, Teams und Organisationseinheiten, überwiegend im Profitbereich. (Internationale Konzerne). Mein Beratungsspektrum ist Führung, Prozessverbesserungen, Teamentwicklung
Aufgabenstellung
Der Text ist in Anlehnung an meine HP, Teamentwicklung und Coaching und es sollte eine übersichtliche, infomative 1-2 Seiten entstehen, die ich als erste Werbung/Kontaktaufnahme versenden kann. Die Seiten sollen klar einen Überblick über mein "Schaffen" geben, sollen aber auch schon etwas von meiner Arbeitsweise deutlich machen. (Ich begriefe schnell, formuliere klar und arbeite sehr zielorientiert - allerdings auch schnörkellos!) Diese Seiten sollten überwiegend als Anhang an eine Mail fungieren, im Ausnahmefall aber auch versendet werden.
Das Logo, die Farbe, etc. analog zu meiner HP - ich lass mich da aber auch gern beraten, falls sie andere Ideen haben

```html
<!DOCTYPE html>
<html lang="de">
<head>
<meta charset="utf-8">
<title>Teamentwicklung</title>
<link rel="stylesheet" href="https://fonts.googleapis.com/css2?family=Open+Sans:wght@400&family=Tinos:wght@700&display=swap">
<style>
  :root {
    --plum: #770a55;
    --band: #b9c6c2;
    --text: #6a6a6a;
    --white: #ffffff;
    --photo: #a9c7c9;
  }
  * { margin: 0; padding: 0; box-sizing: border-box; }
  html, body { width: 1120px; height: 1200px; overflow: hidden; background: var(--white); }
  .flyer { position: relative; width: 1120px; height: 1200px; font-family: "Open Sans", sans-serif; color: var(--text); }

  .pier-photo {
    position: absolute; left: 0; top: 0; width: 683px; height: 1200px;
    background: var(--photo);
  }

  .quote-band { position: absolute; left: 0; top: 60px; width: 1120px; height: 114px; background: var(--band); }
  .quote-frame { position: absolute; left: 0; top: 60px; }
  .quote-text {
    position: absolute; left: 0; top: 60px; width: 500px;
    font-family: "Tinos", serif; font-weight: 700; font-size: 24px; color: var(--white); line-height: 37px;
  }
  .quote-text .line-one { position: absolute; left: 49px; top: 19px; white-space: nowrap; }
  .quote-text .line-two { position: absolute; left: 122px; top: 55px; white-space: nowrap; }

  .accent-bar { position: absolute; left: 939px; top: 0; width: 109px; height: 260px; background: var(--plum); }

  .content { position: absolute; left: 715px; top: 354px; width: 400px; }
  .content h1 { font-weight: 400; font-size: 34px; color: var(--plum); letter-spacing: 0.2px; line-height: 1; margin-bottom: 18px; }
  .content p { font-size: 21px; line-height: 25.4px; }
  .intro { margin-bottom: 39px; }
  .list-lead { margin-bottom: 25px; }
  .benefits { list-style: none; }
  .benefits li { position: relative; padding-left: 26px; font-size: 21px; line-height: 25.4px; margin-bottom: 25px; }
  .benefits li::before {
    content: ""; position: absolute; left: 0; top: 8px; width: 11px; height: 11px; background: var(--plum);
  }
</style>
</head>
<body>
<div class="flyer">
  <div class="pier-photo" role="img" aria-label="Foto: Holzsteg mit weißem Geländer, der über das Meer unter blauem Himmel führt"></div>

  <div class="quote-band"></div>
  <svg class="quote-frame" width="510" height="114" viewBox="0 0 510 114" aria-hidden="true">
    <g fill="none" stroke="#ffffff" stroke-width="3">
      <polyline points="80,9 19,9 19,107 80,107"/>
      <polyline points="425,9 485,9 485,107 425,107"/>
    </g>
    <text x="10" y="42" fill="#ffffff" font-family="Tinos, serif" font-weight="700" font-size="30">“</text>
    <text x="476" y="104" fill="#ffffff" font-family="Tinos, serif" font-weight="700" font-size="30">”</text>
  </svg>
  <blockquote class="quote-text">
    <span class="line-one">Zu erkennen was geschieht,</span>
    <span class="line-two">ist der Beginn der Veränderung.</span>
  </blockquote>

  <div class="accent-bar"></div>

  <section class="content">
    <h1>TEAMENTWICKLUNG</h1>
    <p class="intro">Teams sind lebendige Gebilde, die<br>um erfolgreich zu sein, sich immer<br>wiederneu ausrichten und koordi-<br>nieren müssen. Das tun sie in aller<br>Regel ohne fremde Hilfe - aber<br>ab und zu ist es hilfreich, Impulse<br>oder Entwicklungsförderung von<br>außen bekommen.</p>
    <p class="list-lead">Dazu gehören</p>
    <ul class="benefits">
      <li>Eine sorgfältige Analyse<br>der Situation und Festlegung<br>gewünschter Resultate</li>
      <li>Überzeugende und förderliche<br>Methoden, die die Lösungs<br>kompetenzen der Menschen<br>im Team unterstützen</li>
      <li>Klare Führung durch den<br>Widerstreit von Teaminteres-<br>sen zwischen Verändern, Be-<br>wahren, Harmonie und Kon-<br>fliktbearbeitung, klarem Feed-<br>back und Eintracht im Team</li>
      <li>Tragfähigkeit der Ergebnisse</li>
    </ul>
  </section>
</div>
</body>
</html>
```